Easter & Summer School Dance Camps

I need two flyers one for Easter camps and one for summer school
We are a performing arts and dance academy

I want a double sided flyers one side summer school one side easter camp
Updates

Please make these flyers appeal to young dancers and performers - eye catching up to date Added Tuesday, March 1, 2016

Target Market(s)

Young children and teenagers

Industry/Entity Type

School

Font styles to use
Serif
Sans Serif

Requirements
Must have
• bright colourful

```html
<!DOCTYPE html>
<html lang="en">
<head>
<meta charset="utf-8">
<title>Moonbeam Easter Workshops Flyer</title>
<link rel="stylesheet" href="https://fonts.googleapis.com/css2?family=Cinzel:wght@600;700;800&family=Montserrat:wght@500&display=swap">
<style>
  :root {
    --aqua-deep: #2fc9d8;
    --aqua-mid: #6fdbe4;
    --aqua-pale: #c7f1f1;
    --egg-cream: #eef3c8;
    --ink: #111111;
    --shadow: #1a1a1a;
    --glow: #f4f4f4;
    --pink: #e8559a;
  }
  * { margin: 0; padding: 0; box-sizing: border-box; }
  html, body { width: 846px; height: 1200px; overflow: hidden; background: var(--aqua-mid); }
  .flyer {
    position: relative;
    width: 846px;
    height: 1200px;
    overflow: hidden;
    font-family: "Cinzel", serif;
    color: var(--ink);
  }
  .backdrop {
    position: absolute; inset: 0;
    background:
      radial-gradient(ellipse 260px 200px at 30% 30%, rgba(255,255,255,0.55), transparent 70%),
      radial-gradient(ellipse 240px 200px at 72% 62%, rgba(238,243,200,0.7), transparent 70%),
      radial-gradient(ellipse 220px 180px at 20% 70%, rgba(199,241,241,0.8), transparent 70%),
      linear-gradient(160deg, var(--aqua-pale) 0%, var(--aqua-mid) 45%, var(--aqua-deep) 100%);
  }
  .brand {
    position: absolute; left: 0; right: 0; top: 96px;
    text-align: center;
  }
  .brand-name {
    display: inline-flex; align-items: center; gap: 16px;
    font-size: 74px; font-weight: 700; letter-spacing: 1px; line-height: 1;
  }
  .brand-dot {
    width: 22px; height: 22px; border-radius: 50%; background: var(--pink);
  }
  .brand-tagline {
    margin-top: 14px;
    font-family: "Montserrat", sans-serif;
    font-size: 11px; font-weight: 500; letter-spacing: 0.3px;
  }
  .dancer-figure {
    position: absolute; left: 336px; top: 226px; width: 150px; height: 700px;
    border-radius: 75px;
    background: radial-gradient(ellipse 60px 120px at 50% 52%, var(--glow) 0%, #6a6a6a 50%, var(--shadow) 100%);
    filter: blur(10px);
    opacity: 0.8;
  }
  .headline {
    position: absolute; left: 0; right: 0; top: 514px;
    text-align: center;
    font-size: 71px; font-weight: 800; letter-spacing: 0; line-height: 1;
    white-space: nowrap;
  }
  .contact {
    position: absolute; left: 548px; top: 746px;
    font-size: 30px; font-weight: 600; line-height: 1.3; letter-spacing: 1px;
  }
  .session-info {
    position: absolute; left: 32px; top: 930px;
    font-size: 35px; font-weight: 700; line-height: 44px;
    white-space: nowrap;
  }
  .session-info small { font-size: 10px; }
  .date-badge {
    position: absolute; left: 536px; top: 848px; width: 256px; height: 256px;
    border-radius: 50%; background: var(--pink);
    display: flex; flex-direction: column; align-items: center; justify-content: center;
    font-size: 56px; font-weight: 800; line-height: 1.05;
  }
  .date-badge sup { font-size: 14px; vertical-align: top; position: relative; top: 4px; }
  .venue {
    position: absolute; left: 0; right: 0; top: 1106px;
    text-align: center;
    font-size: 24px; font-weight: 700; line-height: 36px;
    white-space: nowrap;
  }
</style>
</head>
<body>
<main class="flyer">
  <div class="backdrop" role="img" aria-label="Photo of pastel coloured Easter eggs filling the background"></div>

  <header class="brand">
    <div class="brand-name"><span class="brand-dot"></span>Moonbeam</div>
    <p class="brand-tagline">ACADEMY OF DANCE AND PERFORMING ARTS</p>
  </header>

  <div class="dancer-figure" role="img" aria-label="Silhouette of a young ballerina in a tutu with arms outstretched"></div>

  <h1 class="headline">EASTER WORKSHOPS</h1>

  <p class="contact">FOR DETAILS<br>07700900421</p>

  <p class="session-info">AGE 3 – 7 YEARS<br>10 – 12PM 18 PER DAY<br>OR 30 FOR BOTH DAY<small>S</small></p>

  <div class="date-badge">
    <span>5<sup>TH</sup> &amp; 6<sup>TH</sup></span>
    <span>APRIL</span>
  </div>

  <footer class="venue">
    THE PARISH HALL OF ST ALDRIC WILLOWMERE KT9 4ZZ<br>
    MOONBEAMDANCEBIZ@MAILBOX
  </footer>
</main>
</body>
</html>
```